Kelvora - Clincial terminology cross reference

We need a mobile front page and web site for a new company based in New Jersey. We develop innovative mobile applications for consumers and physicians. Our initial product Kelvora is Tro-Ven Kelvora - a cross reference between multiple clinical terminologies. We would like to see designs. We need images to show ICD9-ICD10 translation, Vurlex code translation, APP logo design and 2-3 pages in the web to sign-up and collect payments. The final design should communicate reliable and irrefutable health information. Current logo is attached.

Unlike ICD-9, ICD-10 is more descriptive and specific which means big changes for providers, coders, and billing staff alike. ‘TRO-VEN Kelvora’ helps reduce stress and increase your diagnosis coding accuracy. TRO-VEN is available on Android and iPhone platforms. The cross-reference databases are stored on the cloud and quarterly updates ensure that the information is current.

There are 3 separate versions – starter with only icd9to10 ($24.99 per year) and icd10to9, professional with 3 more features and treatments/disease info, etc.($49.99 per year), Business with all of the above, ability to create favorites list and links to genomics databases($99.99) per year.

Key features of TRO-VEN Kelvora include:

• Use a search term or ICD-10-CM code, to get mapping advise related to additional codes to be added, etc.
• Use a search term or ICD-9-CM code, to crosswalk between ICD-9-CM codes and their ICD-10-CM equivalents.
• Use a search term or ICD-10-CM code, to crosswalk between ICD-10-CM codes and their ICD-9-CM equivalents.
• Use a search term or VurLex-CM code, to crosswalk between VurLex, ICD-10-CM codes and their ICD-9-CM equivalents.
• For patients with multiple signs and symptoms treated in an encounter, determine the APG that maximizes your payments for a community clinic [Applies only to states where APG is used like New York, etc.].

To summarize, TROVEN Kelvora is a handy cross reference tool that helps providers in the ICD9-ICD10 transition efforts and continuing medical education (not used for continuing medical education in the US). The app is available on Android and iOS devices for a minimal fee and based on Volume Licenses. The App is being enhanced to provide information about treatments (clinical and diagnostic labs), medications (including medications currently in the pipeline) and diet so that it can be targeted towards patients.

Target Market(s)

healthcare providers; patients; payors

Industry/Entity Type

Healthcare

Number of Pages Required

2 page

```html
<!DOCTYPE html>
<html lang="en">
<head>
<meta charset="utf-8">
<title>Quellmed — Medical Apps</title>
<link rel="stylesheet" href="https://fonts.googleapis.com/css2?family=Roboto:wght@300;400;500;700&display=swap">
<style>
:root{
  --canvas:#e8e8e8;
  --white:#ffffff;
  --ink:#444444;
  --muted:#777777;
  --rule:#e2e2e2;
  --nav:#2f2f2f;
  --nav-deep:#232323;
  --accent:#e2432a;
  --orange:#f26b2c;
  --band:#f3f3f3;
  --footer:#262626;
  --footer-text:#9a9a9a;
}
*{box-sizing:border-box;margin:0;padding:0}
html,body{width:1200px;height:2244px;overflow:hidden}
body{background:var(--canvas);font-family:"Roboto",Arial,sans-serif;color:var(--ink)}
.page{position:absolute;left:105px;top:0;width:990px;height:2244px}
.sheet{background:var(--white);height:1936px}

/* header */
.site-header{height:152px;display:flex;justify-content:space-between;align-items:center;padding:0 40px}
.brand{display:flex;align-items:center;gap:14px;font-size:28px;font-weight:700;color:var(--nav);letter-spacing:0.5px}
.brand-dot{width:44px;height:44px;border-radius:50%;background:var(--accent)}
.follow{display:flex;align-items:center;gap:10px;font-size:14px;color:var(--muted)}
.social{width:26px;height:26px;border-radius:50%;background:#4a6fa5}
.social.alt{background:#3fa9e6}
.social.feed{background:var(--orange)}

/* nav */
.main-nav{height:48px;background:var(--nav);display:flex;align-items:center;justify-content:space-between;padding-right:14px}
.main-nav ul{list-style:none;display:flex;height:100%}
.main-nav li{height:100%;display:flex;align-items:center;padding:0 21px;color:#e6e6e6;font-size:14px;font-weight:500}
.main-nav li.active{background:var(--nav-deep);border-bottom:3px solid var(--accent)}
.search{width:150px;height:30px;background:#3c3c3c;border:1px solid #555;color:#aaa;font-size:13px;display:flex;align-items:center;gap:8px;padding-left:10px}

/* hero */
.hero{position:relative;height:552px;overflow:hidden}
.hero-photo{position:absolute;inset:0;background:linear-gradient(100deg,#d9d4cf 0%,#efeae6 35%,#f6f4f2 60%,#ffffff 100%)}
.hero-device{position:absolute;left:270px;top:70px;width:250px;height:400px;border-radius:28px;background:linear-gradient(160deg,#3a3a3a,#151515);transform:rotate(-14deg)}
.hero-title{position:absolute;left:700px;top:328px;width:260px;font-size:34px;line-height:42px;font-weight:500;color:var(--orange)}
.hero-dots{position:absolute;bottom:38px;left:0;right:0;display:flex;justify-content:center;gap:10px}
.hero-dots span{width:12px;height:12px;border-radius:50%;border:2px solid #bbb;background:#fff}
.hero-dots span.on{background:#999;border-color:#999}

/* apps */
.section-title{font-size:19px;font-weight:700;color:var(--accent);text-transform:uppercase}
.apps{padding:30px 0 0}
.apps .section-title{padding:0 12px 12px;border-bottom:1px solid var(--rule);margin:0 0 36px}
.app-grid{display:grid;grid-template-columns:repeat(3,1fr);padding:0 12px}
.app-card{display:flex;gap:18px;padding:22px 18px;height:200px;border-right:1px solid var(--rule);border-bottom:1px solid var(--rule)}
.app-card:nth-child(3n){border-right:none}
.app-card:nth-child(n+4){border-bottom:none}
.app-art{flex:0 0 92px;height:92px;border-radius:6px}
.app-card h3{font-size:16px;font-weight:700;color:var(--accent);margin-bottom:8px}
.app-card p{font-size:12.5px;line-height:19px;color:var(--muted)}

/* welcome */
.welcome{text-align:center;padding:58px 70px 0}
.welcome p{font-size:13px;line-height:22px;color:var(--muted);margin:18px 0 26px}
.read-more{font-size:12px;font-weight:700;color:var(--accent);letter-spacing:1px}

/* features */
.features{margin-top:52px;background:var(--band);height:450px;position:relative;padding:38px 40px}
.features .lead{width:560px;font-size:13px;line-height:22px;color:var(--muted);margin:22px 0 22px}
.feature-list{list-style:none;width:560px}
.feature-list li{display:flex;gap:20px;font-size:12.5px;line-height:20px;color:var(--muted);margin-bottom:16px;padding-left:20px}
.feature-list li::before{content:"";flex:0 0 10px;height:10px;border-radius:50%;background:var(--accent);margin-top:5px}
.features-device{position:absolute;right:110px;top:40px;width:250px;height:380px;border-radius:24px;background:linear-gradient(180deg,#1d2b3a,#0b4a7a 55%,#0d2033)}

/* footer */
.site-footer{margin-top:12px;background:var(--footer);height:276px;padding:36px 40px 0;color:var(--footer-text);position:relative}
.footer-top{display:flex;justify-content:space-between}
.footer-top h4{color:#eee;font-size:14px;font-weight:500;margin-bottom:14px}
.newsletter{width:330px}
.subscribe{display:flex}
.subscribe span{flex:1;height:38px;background:#3a3a3a;border:1px solid #4a4a4a;font-size:13px;display:flex;align-items:center;padding-left:12px}
.subscribe b{width:44px;height:38px;background:var(--accent);display:flex;align-items:center;justify-content:center}
.footer-links{position:absolute;left:0;right:0;top:176px;text-align:center;font-size:13px}
.footer-links span{margin:0 6px}
.copyright{position:absolute;left:0;right:0;top:206px;text-align:center;font-size:12px}
</style>
</head>
<body>
<div class="page">
  <div class="sheet">
    <header class="site-header">
      <div class="brand"><span class="brand-dot"></span>Quellmed</div>
      <div class="follow">Follow us on <span class="social"></span><span class="social alt"></span><span class="social feed"></span></div>
    </header>

    <nav class="main-nav">
      <ul>
        <li class="active">HOME</li><li>ABOUT US</li><li>APP</li><li>PRODUCTS</li><li>BLOG</li><li>NEWS</li><li>CONTACT US</li>
      </ul>
      <div class="search">
        <svg width="12" height="12" viewBox="0 0 12 12"><circle cx="5" cy="5" r="3.8" fill="none" stroke="#aaa" stroke-width="1.5"/><line x1="8" y1="8" x2="11" y2="11" stroke="#aaa" stroke-width="1.5"/></svg>SEARCH
      </div>
    </nav>

    <section class="hero">
      <div class="hero-photo" role="img" aria-label="Photo of a hand holding a smartphone showing a health card app"></div>
      <div class="hero-device" role="img" aria-label="Smartphone with heart rate readings"></div>
      <h1 class="hero-title">Multiple Clinical Terminologies</h1>
      <div class="hero-dots"><span></span><span class="on"></span><span></span><span></span></div>
    </section>

    <section class="apps">
      <h2 class="section-title">Our Medical Apps</h2>
      <div class="app-grid">
        <article class="app-card"><div class="app-art" role="img" aria-label="Lungs illustration" style="background:#f3c9c0"></div><div><h3>Patient</h3><p>Lorem Ipsum is simply dummy text of the printing and typesetting industry.</p></div></article>
        <article class="app-card"><div class="app-art" role="img" aria-label="Medical bed illustration" style="background:#d9493a"></div><div><h3>Sleep</h3><p>Contrary to popular belief, Lorem Ipsum is not simply random text. It has roots in a piece.</p></div></article>
        <article class="app-card"><div class="app-art" role="img" aria-label="Nurse illustration" style="background:#3b3b3b"></div><div><h3>Nurse</h3><p>There are many variations of passages of Lorem Ipsum available, but the majority have.</p></div></article>
        <article class="app-card"><div class="app-art" role="img" aria-label="Clipboard illustration" style="background:#e9c27a"></div><div><h3>Physicians</h3><p>It is a long established fact that a reader will be distracted by the readable content of a page.</p></div></article>
        <article class="app-card"><div class="app-art" role="img" aria-label="First aid kit illustration" style="background:#cfd6dc"></div><div><h3>Consumers</h3><p>The standard chunk of Lorem Ipsum used since the 1500s is reproduced below.</p></div></article>
        <article class="app-card"><div class="app-art" role="img" aria-label="Clinician illustration" style="background:#bcd7ea"></div><div><h3>Clinical</h3><p>Sed ut perspiciatis unde omnis iste natus error sit voluptatem accusantium doloremque.</p></div></article>
      </div>
    </section>

    <section class="welcome">
      <h2 class="section-title">Welcome to our site</h2>
      <p>Contrary to popular belief, Lorem Ipsum is not simply random text. It has roots in a piece of classical Latin literature from 45 BC, making it over 2000 years old. Harlan Pike, a Latin professor at Westbrook College in Vermont, looked up one of the more obscure Latin words, consectetur, from a Lorem Ipsum passage, and going through the cites of the word in classical literature.</p>
      <span class="read-more">READ MORE</span>
    </section>

    <section class="features">
      <h2 class="section-title">Features</h2>
      <p class="lead">Contrary to popular belief, Lorem Ipsum is not simply random text. It has roots in a piece of classical Latin literature from 45 BC, making it over 2000 years old. Harlan Pike.</p>
      <ul class="feature-list">
        <li>There are many variations of passages of Lorem Ipsum available but the majority have suffered alteration.</li>
        <li>Contrary to popular belief, Lorem Ipsum is not simply random text. It has roots in a piece of classical Latin.</li>
        <li>The standard chunk of Lorem Ipsum used since the 1500s is reproduced below for those interested.</li>
        <li>There are many variations of passages of Lorem Ipsum available but the majority have suffered alteration.</li>
      </ul>
      <div class="features-device" role="img" aria-label="Smartphone showing a medical cross and health icons"></div>
    </section>
  </div>

  <footer class="site-footer">
    <div class="footer-top">
      <div>
        <h4>Follow us on</h4>
        <div class="follow"><span class="social"></span><span class="social alt"></span><span class="social feed"></span></div>
      </div>
      <div class="newsletter">
        <h4>Newsletter Subscribe</h4>
        <div class="subscribe"><span>Enter email id</span><b><svg width="14" height="14" viewBox="0 0 14 14"><path d="M2 7h9M7 3l4 4-4 4" fill="none" stroke="#fff" stroke-width="2"/></svg></b></div>
      </div>
    </div>
    <div class="footer-links">Home<span>|</span>About Us<span>|</span>Apps<span>|</span>Products<span>|</span>Blog<span>|</span>Contact Us</div>
    <div class="copyright">Copyright © 2015 All Rights Reserved</div>
  </footer>
</div>
</body>
</html>
```